Wendell Gallery 2018-2019 Season brochure

Each summer we announce our lineup of 6 exhibits for the next season. This brochure also includes information about our satellite galleries and events. The brochure always ends up being a quad-fold (rather than a tri-fold). Each of the exhibits includes a photograph and description. This next year our exhibits include a TBA (Sep 15 – Oct 20 2018), 63rd Ridgeline Painters' Showcase (Nov 3 - Dec. 8), Corvath Exhibit (Jan 17 – Feb 23 2019), 41st Open Lens Camera Salon (Mar 10 – Apr 14), SaMB - Faculty & Student Exhibition (April 30 - May 25, 2019), WGG Membership Show (Jun 8- June 29, 2019.)

You will see the brown/orange brochure that has much of the same info. We will still Thimble, Hotel Brackley, and Pemway Vineyards satellite galleries. A membership form. (the Gallery is Wendell Gallery, the membership is Wendell Gallery Guild) We will have a Member's Event, Spark Walk, and Porch Crawl. We will not have the Bravo event, but have a Porch Crawl Preview event.

I have attached the 2017-18 brochure and previous brochures. I am looking for something fresh and new and not brown and orange as before.

I am attaching the 2015-16 brochure which was cut at an angle at the top so that it layered at an angle.

Our Vision statement is "Growing a passion for Craft"

Target Market(s)

Art Gallery goers

Font styles to use
Sans Serif

Colors

Designer to choose colors to be used in the design.

Requirements
Must have
• 6 exhibits with photos, membership form, special events, satellite galleries. See 17-18 brochure for basic info
Nice to have
• We seem to be having a lot of brilliant multicolored exhibits next year.

```html
<!DOCTYPE html>
<html lang="en">
<head>
<meta charset="utf-8">
<title>Wendell Gallery 2018–2019 Season Brochure</title>
<link href="https://fonts.googleapis.com/css2?family=Oswald:wght@400;600&family=Open+Sans:wght@400;600;700&display=swap" rel="stylesheet">
<style>
:root{
  --bg:#e8e8e8;
  --wine-dark:#3e080c;
  --wine:#6d1219;
  --wine-light:#8c1d25;
  --gold:#f2a51e;
  --orange:#e2661c;
  --cream:#f7ecd9;
  --text:#f3e6e0;
  --muted:#d9b9b0;
  --label:#9a9a9a;
}
*{box-sizing:border-box;margin:0;padding:0}
html,body{width:1200px;height:2172px;overflow:hidden}
body{background:var(--bg);font-family:"Open Sans",sans-serif;color:var(--text);position:relative}
.side-label{position:absolute;right:20px;font-family:"Oswald",sans-serif;font-size:20px;letter-spacing:3px;color:var(--label)}
.side-label.outside{top:374px}
.side-label.inside{top:1812px}
.spread{position:absolute;left:20px;width:1160px;height:667px;display:grid;grid-template-columns:repeat(4,1fr);box-shadow:0 6px 18px rgba(0,0,0,.25)}
.spread.outside{top:410px}
.spread.inside{top:1137px}
.panel{position:relative;padding:18px 18px 16px;background:radial-gradient(ellipse at 50% 45%,var(--wine-light),var(--wine) 55%,var(--wine-dark));border-right:1px solid rgba(0,0,0,.35);display:flex;flex-direction:column;gap:10px;overflow:hidden;min-width:0}
.panel:last-child{border-right:none}
.band{margin:0 -18px;padding:5px 18px;background:linear-gradient(90deg,var(--orange),var(--gold));font-family:"Oswald",sans-serif;font-weight:600;font-size:17px;letter-spacing:1px;color:var(--wine-dark);text-transform:uppercase}
h3{font-family:"Oswald",sans-serif;font-weight:600;font-size:19px;line-height:1.1;color:var(--cream);text-transform:uppercase}
.date{font-family:"Oswald",sans-serif;font-size:12px;letter-spacing:1px;color:var(--gold);text-transform:uppercase}
p{font-size:10.5px;line-height:1.45;color:var(--text)}
.small{font-size:9.5px;color:var(--muted)}
.photo{border-radius:2px;flex-shrink:0}
.photo.warm{background:linear-gradient(135deg,#c9813a,#5b3a2a)}
.photo.cool{background:linear-gradient(135deg,#5f8fa8,#2d3f4d)}
.photo.bright{background:linear-gradient(135deg,#e34f6b,#f0c23c 50%,#3aa6b9)}
.photo.green{background:linear-gradient(135deg,#6d9a4b,#2f4a2a)}
.photo.grey{background:linear-gradient(135deg,#9c9690,#4a4440)}
.row{display:flex;gap:10px;align-items:flex-start}
.wordmark{font-family:"Oswald",sans-serif;font-weight:600;font-size:24px;letter-spacing:2px;color:var(--cream);text-transform:uppercase;line-height:1.05}
.wordmark.large{font-size:38px}
.form-grid{display:grid;grid-template-columns:1fr 1fr;gap:4px 10px;font-size:9.5px;color:var(--cream)}
.form-grid span{border-bottom:1px solid rgba(247,236,217,.5);padding-bottom:2px}
.contact{font-size:10px;color:var(--cream);line-height:1.5}
.cover .season{font-family:"Oswald",sans-serif;font-size:14px;color:var(--gold);letter-spacing:2px;margin-top:-6px}
.cover .hero{width:100%;height:210px;margin:22px 0 8px;background:linear-gradient(135deg,#7aa35c,#c07a3a 60%,#5a3a28)}
.vision{font-family:"Oswald",sans-serif;font-size:24px;line-height:1.15;color:var(--cream);text-transform:uppercase;letter-spacing:1px;margin-top:8px}
.foot{margin-top:auto}
.gallery-item{display:flex;flex-direction:column;gap:6px}
.hours{display:grid;grid-template-columns:auto 1fr;gap:2px 8px;font-size:9.5px;color:var(--cream)}
</style>
</head>
<body>

<div class="side-label outside">OUTSIDE</div>

<section class="spread outside">
  <article class="panel membership">
    <div class="band">Membership</div>
    <div class="wordmark">Wendell Gallery Guild</div>
    <p>Join the Wendell Gallery Guild and help bring bold new art to our valley. Members enjoy previews, events and discounts.</p>
    <div class="form-grid">
      <span>Name</span><span>Phone</span>
      <span>Address</span><span>Email</span>
      <span>City / Zip</span><span>Level</span>
    </div>
    <p class="small">Individual $40 · Family $60 · Patron $150 · Benefactor $500</p>
    <div class="photo cool" role="img" aria-label="Street map showing the gallery location" style="height:170px"></div>
    <div class="contact">210 Orchard Lane, Ridgeline<br>(555) 014-2290<br>wendellgallery.org</div>
  </article>

  <article class="panel events">
    <div class="band">Events</div>
    <h3>Members' Event</h3>
    <div class="date">September 22, 2018</div>
    <div class="row">
      <p>An evening for guild members to meet the artists and preview the season ahead.</p>
      <div class="photo warm" role="img" aria-label="Guests at a members' evening" style="width:92px;height:70px"></div>
    </div>
    <h3>Porch Crawl Preview</h3>
    <div class="date">April 2019</div>
    <p>A first look at the homes and studios on this year's crawl, with light refreshments.</p>
    <h3>Spark Walk</h3>
    <div class="date">January 26, 2019</div>
    <div class="photo bright" role="img" aria-label="Colourful lit artwork at the night walk" style="height:120px"></div>
    <p>Galleries open late with lights, music and art across downtown.</p>
  </article>

  <article class="panel tour">
    <div class="band">Porch Crawl</div>
    <div class="date">May 18, 2019</div>
    <p>Step inside the homes of local artists and collectors. Self-guided tour, tickets at the gallery.</p>
    <div class="photo warm" role="img" aria-label="Interior of an artist's home" style="height:120px"></div>
    <div class="row">
      <div class="photo grey" role="img" aria-label="Sculpture on a porch" style="width:120px;height:90px"></div>
      <div class="photo green" role="img" aria-label="Garden studio" style="width:120px;height:90px"></div>
    </div>
    <p class="small">Tickets $25 · Members $20 · 10 am – 4 pm</p>
    <div class="foot wordmark">Wendell</div>
  </article>

  <article class="panel cover">
    <div class="wordmark large">Wendell</div>
    <div class="season">2018–2019</div>
    <div class="photo hero" role="img" aria-label="Photograph of the gallery building"></div>
    <div class="vision">Growing a passion<br>for Craft</div>
    <p class="small foot">Wendell Gallery · 2018–2019 Season</p>
  </article>
</section>

<section class="spread inside">
  <article class="panel">
    <div class="band">Exhibitions</div>
    <h3>Harvest Table</h3>
    <div class="date">Sep 15 – Oct 20, 2018</div>
    <div class="photo warm" role="img" aria-label="Food displayed on a table" style="height:120px"></div>
    <p>Photographs of meals and markets from kitchens around the world.</p>
    <h3>63rd Ridgeline Painters' Showcase</h3>
    <div class="date">Nov 3 – Dec 8, 2018</div>
    <div class="photo bright" role="img" aria-label="Bright abstract painting" style="height:120px"></div>
    <p>Regional painters share new work in every medium.</p>
  </article>

  <article class="panel">
    <h3>Mysteries of the Corvath</h3>
    <div class="date">Jan 17 – Feb 23, 2019</div>
    <div class="photo green" role="img" aria-label="Rainforest artifacts" style="height:130px"></div>
    <p>Objects, masks and textiles from deep river cultures.</p>
    <h3>41st Open Lens Camera Salon</h3>
    <div class="date">Mar 10 – Apr 14, 2019</div>
    <div class="photo cool" role="img" aria-label="Juried landscape photograph" style="height:130px"></div>
    <p>Juried photography from artists across the nation.</p>
  </article>

  <article class="panel">
    <h3>SaMB – Faculty &amp; Student Exhibition</h3>
    <div class="date">April 30 – May 25, 2019</div>
    <div class="photo bright" role="img" aria-label="Student ceramic and painted works" style="height:130px"></div>
    <p>Work by faculty and students of the visual arts program.</p>
    <h3>WGG Membership Show</h3>
    <div class="date">June 8 – June 29, 2019</div>
    <div class="photo grey" role="img" aria-label="Members' artworks on gallery walls" style="height:130px"></div>
    <p>Our guild members show their best work of the year.</p>
  </article>

  <article class="panel">
    <div class="band">Galleries</div>
    <div class="gallery-item">
      <h3>Pemway Vineyards</h3>
      <div class="row">
        <div class="hours"><span>Sep 15</span><span>Oct 20</span><span>Nov 3</span><span>Dec 8</span></div>
        <div class="photo warm" role="img" aria-label="Painting at the winery tasting room" style="width:130px;height:80px"></div>
      </div>
    </div>
    <div class="gallery-item">
      <h3>Hotel Brackley</h3>
      <div class="photo grey" role="img" aria-label="Art in the hotel lobby" style="height:110px"></div>
      <p class="small">Rotating exhibits in the lobby, open daily.</p>
    </div>
    <div class="gallery-item">
      <h3>Thimble</h3>
      <div class="photo bright" role="img" aria-label="Colourful textile artwork" style="height:110px"></div>
      <p class="small">Local makers on show, Tue – Sat.</p>
    </div>
  </article>
</section>

<div class="side-label inside">INSIDE</div>

</body>
</html>
```